" Modo tradicional de funcionamento de drogarias, com diversas seções de produtos, mas evidentemente tendo como principal produto a comercialização de medicamentos. "

```html
<!DOCTYPE html>
<html lang="pt-BR">
<head>
<meta charset="utf-8">
<title>VitaPonte Drogaria — Cartão de visita</title>
<link rel="stylesheet" href="https://fonts.googleapis.com/css2?family=Montserrat:wght@500;600;700;800&display=swap">
<style>
  :root {
    --brand-blue: #1f3fc4;
    --brand-blue-deep: #1a34a3;
    --brand-yellow: #f3c21b;
    --tint-yellow: #f8e6a6;
    --tint-blue: #b7c6e2;
    --paper: #ffffff;
    --ink: #1f3fc4;
    --backdrop: #e9ebef;
  }
  * { box-sizing: border-box; margin: 0; padding: 0; }
  html, body { width: 1200px; height: 1200px; overflow: hidden; }
  body {
    background: var(--backdrop);
    font-family: "Montserrat", sans-serif;
    display: flex;
    flex-direction: column;
    align-items: center;
    justify-content: center;
    gap: 70px;
  }
  .card {
    width: 900px;
    height: 500px;
    border-radius: 34px;
    position: relative;
    overflow: hidden;
    box-shadow: 0 10px 30px rgba(20, 30, 70, 0.15);
  }

  /* Front */
  .card--front {
    background: var(--brand-blue);
    display: flex;
    align-items: center;
    justify-content: center;
  }
  .brand {
    display: flex;
    flex-direction: column;
    align-items: flex-end;
    color: var(--paper);
  }
  .brand__row { display: flex; align-items: center; gap: 22px; }
  .brand__name { font-weight: 800; font-size: 96px; letter-spacing: -2px; line-height: 1; white-space: nowrap; }
  .brand__dot { width: 56px; height: 56px; border-radius: 50%; background: var(--paper); }
  .brand__tag { font-weight: 500; font-size: 26px; letter-spacing: 14px; margin-top: 6px; margin-right: -14px; }

  /* Back */
  .card--back { background: var(--paper); }
  .back__shapes { position: absolute; left: 0; top: 0; width: 300px; height: 500px; }
  .back__name {
    position: absolute; left: 330px; top: 52px;
    font-weight: 700; font-size: 24px; line-height: 1; color: var(--ink); letter-spacing: 1px;
    white-space: nowrap;
  }
  .back__brand {
    position: absolute; right: 60px; top: 100px;
    display: flex; flex-direction: column; align-items: flex-end; color: var(--ink);
  }
  .back__brand .brand__name { font-size: 64px; letter-spacing: -1px; }
  .back__brand .brand__tag { font-size: 17px; letter-spacing: 10px; margin-right: -10px; }
  .contact {
    position: absolute; right: 60px; top: 240px;
    list-style: none; text-align: right; color: var(--ink);
    font-weight: 500; font-size: 19px; line-height: 1.5;
  }
  .contact li { display: flex; justify-content: flex-end; align-items: center; gap: 12px; white-space: nowrap; }
  .contact__bullet { width: 14px; height: 14px; border-radius: 50%; background: var(--brand-yellow); flex: none; }
  .contact__gap { height: 12px; }
  .back__band {
    position: absolute; left: 0; right: 0; bottom: 0; height: 34px;
    background: var(--brand-blue-deep);
  }
</style>
</head>
<body>
  <section class="card card--front" aria-label="Frente do cartão">
    <div class="brand">
      <div class="brand__row">
        <span class="brand__name">VitaPonte</span>
        <span class="brand__dot"></span>
      </div>
      <span class="brand__tag">DROGARIA</span>
    </div>
  </section>

  <section class="card card--back" aria-label="Verso do cartão">
    <svg class="back__shapes" viewBox="0 0 300 500" aria-hidden="true">
      <rect x="0" y="40" width="170" height="150" fill="var(--tint-yellow)"/>
      <polygon points="250,120 150,230 250,340 250,280 210,230 250,180" fill="var(--tint-blue)"/>
      <rect x="0" y="190" width="120" height="90" fill="var(--tint-blue)" opacity="0.6"/>
    </svg>

    <p class="back__name">NOME SOBRENOME</p>

    <div class="back__brand">
      <span class="brand__name">VitaPonte</span>
      <span class="brand__tag">DROGARIA</span>
    </div>

    <ul class="contact">
      <li>R. Exemplo Rua nº 00 - Bairro Nome</li>
      <li>Cidade - UF - CEP: 00000-000</li>
      <li class="contact__gap"></li>
      <li>exemplo@email.com.br<span class="contact__bullet"></span></li>
      <li>www.exemplodesite.com.br<span class="contact__bullet"></span></li>
      <li>00 99999-9999<span class="contact__bullet"></span></li>
      <li>00 99999-9999<span class="contact__bullet"></span></li>
    </ul>

    <div class="back__band"></div>
  </section>
</body>
</html>
```